Business card design for a teacher - double sided, sleek design.

My name is Lina and I am an online Arabic language teacher. I am looking for a beautiful business card design for my online teaching business.

The cards will be printed in 85mm x 55mm size.
The card can be either portrait or landscape.

The design should contain my logo on one side and information on the other.

The design needs to be clean and modern. Use of subtle Arabic geometric patterns would be nice. Icons for the social media information on the card should also match the design theme.

My logo font is Consolas, which is a Monospace font.

Business card design should be delivered with editable PSD or EPS files in the handover.

Thanks

Lina

----

Information on the back:

URL: www.speakwithlina.net [this should stand out more than other details]
Email: info@speakwithlina.net
Instagram: @speakwithlina
Facebook: facebook.com/speakwithlina
Skype: speakwithlina

My brand colours are shown in the logo attached. These are:
- Teal green - 4DC9C1
- Mango yellow - FFD600

Target Market(s)

- Young professionals
- Expatriates
- Women and Men

Industry/Entity Type

Education

Contact Information for Business Card

Information on the back:

Skype: speakwithlina

- Teal green - 4DC9C1
- Mango yellow - FFD600

Font styles to use
Other font styles liked:
• Any font complimentary to my logo font which is a Monospace font called Consolas.

Colors

Designer to choose colors to be used in the design.

Requirements
Must have
• - Aesthetically pleasing look
• - Complimentary design with existing logo
Nice to have
• Arabic geometrical patterns

```html
<!DOCTYPE html>
<html lang="en">
<head>
<meta charset="utf-8">
<title>Qalam Studio – Business Card</title>
<link rel="stylesheet" href="https://fonts.googleapis.com/css2?family=Roboto:wght@400;700&display=swap">
<style>
  :root {
    --teal: #4dc9c1;
    --teal-card: #54c4bc;
    --mango: #ffd600;
    --paper: #ffffff;
    --ink: #4a4a4a;
    --stage: #2a2a2a;
  }
  * { margin: 0; padding: 0; box-sizing: border-box; }
  html, body { width: 1200px; height: 960px; overflow: hidden; }
  body { background: var(--stage); position: relative; font-family: "Roboto", Arial, sans-serif; }

  .card { position: absolute; overflow: hidden; }

  /* Front: contact side */
  .card--front { left: 122px; top: 320px; width: 578px; height: 330px; background: var(--teal-card); }
  .card--front .swoosh { position: absolute; inset: 0; }
  .brand-lockup { position: absolute; left: 42px; top: 46px; display: flex; align-items: center; gap: 14px; }
  .brand-square { display: block; }
  .card--front .brand-square { width: 70px; height: 70px; border: 2px solid var(--paper); }
  .brand-name { font-weight: 400; white-space: nowrap; }
  .card--front .brand-name { font-size: 24px; color: var(--paper); }

  .big-name { position: absolute; font-weight: 700; color: var(--teal); line-height: 1; white-space: nowrap; }
  .card--front .big-name { right: 30px; top: 100px; font-size: 84px; }

  .contact-list { position: absolute; left: 40px; top: 199px; list-style: none; }
  .contact-list li { display: flex; align-items: center; gap: 8px; height: 18.3px; color: var(--paper); font-size: 14px; }
  .contact-list svg { width: 12px; height: 12px; flex: none; }

  /* Back: brand side */
  .card--back { left: 739px; top: 197px; width: 332px; height: 578px; background: var(--paper); }
  .card--back .corner { position: absolute; left: 0; bottom: 0; }
  .back-lockup { position: absolute; left: 0; right: 0; top: 43px; display: flex; flex-direction: column; align-items: center; gap: 10px; }
  .card--back .brand-square { width: 142px; height: 142px; border: 3px solid var(--mango); }
  .card--back .brand-name { font-size: 15px; color: var(--teal); }
  .web-address {
    position: absolute; left: 0; right: 0; top: 235px; text-align: center;
    font-size: 13.5px; letter-spacing: 1.6px; color: var(--ink);
  }
  .web-address strong { font-weight: 700; }
  .card--back .big-name { left: 34px; bottom: 90px; font-size: 92px; }
</style>
</head>
<body>

<section class="card card--front" aria-label="Front of card with contact details">
  <svg class="swoosh" width="578" height="330" viewBox="0 0 578 330" aria-hidden="true">
    <defs>
      <radialGradient id="paperGlow" cx="0.35" cy="0.45" r="0.8">
        <stop offset="0" stop-color="#ffffff"/>
        <stop offset="1" stop-color="#e6e6e6"/>
      </radialGradient>
    </defs>
    <path d="M348 0 C300 60 330 120 280 160 C200 220 230 300 390 330 L578 330 L578 0 Z" fill="url(#paperGlow)"/>
  </svg>

  <div class="brand-lockup">
    <span class="brand-square"></span>
    <p class="brand-name">Qalam Studio</p>
  </div>

  <p class="big-name">Qalam</p>

  <ul class="contact-list">
    <li>
      <svg viewBox="0 0 12 12" aria-hidden="true"><rect x="0.5" y="2" width="11" height="8" fill="none" stroke="#fff"/><path d="M0.5 2 L6 6.5 L11.5 2" fill="none" stroke="#fff"/></svg>
      info@speakwithlina.net
    </li>
    <li>
      <svg viewBox="0 0 12 12" aria-hidden="true"><rect width="12" height="12" fill="#fff"/></svg>
      @speakwithlina
    </li>
    <li>
      <svg viewBox="0 0 12 12" aria-hidden="true"><rect width="12" height="12" fill="#fff"/></svg>
      /speakwithlina
    </li>
    <li>
      <svg viewBox="0 0 12 12" aria-hidden="true"><circle cx="6" cy="6" r="6" fill="#fff"/></svg>
      speakwithlina
    </li>
    <li>
      <svg viewBox="0 0 12 12" aria-hidden="true"><circle cx="6" cy="6" r="5.3" fill="none" stroke="#fff" stroke-width="1.3"/><ellipse cx="6" cy="6" rx="2.3" ry="5.3" fill="none" stroke="#fff"/><path d="M0.7 6 H11.3" stroke="#fff"/></svg>
      www.speakwithlina.net
    </li>
  </ul>
</section>

<section class="card card--back" aria-label="Back of card with brand">
  <svg class="corner" width="60" height="90" viewBox="0 0 60 90" aria-hidden="true">
    <path d="M0 0 C10 30 30 70 60 90 L0 90 Z" fill="var(--mango)"/>
  </svg>

  <div class="back-lockup">
    <span class="brand-square"></span>
    <p class="brand-name">Qalam Studio</p>
  </div>

  <p class="web-address">WWW.<strong>SPEAKWITHLINA</strong>.NET</p>

  <p class="big-name">Qalam</p>
</section>

</body>
</html>
```